依頼詳細
封筒2種類(角2・長3)のデザインをお願いします。
会社のロゴは決まったものがあります。
名刺デザインを踏襲したようなデザインが希望です。
記載項目
添付する名刺同様に、名刺の表の内容を表に、裏の内容を裏にお願いします
表は4Cで結構ですが、裏は1Cでお願いします。
希望イメージ
シンプル 複雑
単色 カラフル
暗い 明るい
日常 高級
遊び心 厳粛
未来的 伝統的
女性的 男性的
希望する色
青系、ベースは白でブルー系でお願いします。
納品ファイル
• イラストレーター形式 (.ai)
補足説明
ロゴは仕様書がありますので添付します。
名刺のデザインを添付します。
■ 選んだ理由

この度はご提案・ご修正等、スムーズにご対応いただきまして誠にありがとうございます。検討したました結果、tokirenaさんにお願いすることにいたしました。23件ご提案をいただきまして、皆さんキレイなデザインで大きな違いはなく、非常に迷いましたが、数案バリエーションでご提案いただき、レスポンスが良かった点が決めてでした。

■ 提案者全員のお礼・コメント

この度はご提案・ご修正等、スムーズにご対応いただきまして誠にありがとうございます。23件ご提案をいただきまして、皆さんキレイなデザインで大きな違いはなく、非常に迷いましたが、数案バリエーションでご提案いただき、レスポンスが良かった点が決めてでした。

```html
<!DOCTYPE html>
<html lang="ja">
<head>
<meta charset="utf-8">
<title>Kaiho Works — Envelope Back</title>
<link rel="stylesheet" href="https://fonts.googleapis.com/css2?family=Open+Sans:wght@400;700&family=Noto+Sans+JP:wght@400&display=swap">
<style>
  :root {
    --paper: #ffffff;
    --line: #b9bcc0;
    --brand-blue: #1f4fa0;
    --note-grey: #666a70;
  }
  html, body {
    margin: 0;
    padding: 0;
    overflow: hidden;
    background: var(--paper);
  }
  .sheet {
    position: relative;
    width: 849px;
    height: 1200px;
    background: var(--paper);
    font-family: "Open Sans", sans-serif;
  }
  .sheet-note {
    position: absolute;
    top: 150px;
    left: 0;
    width: 100%;
    text-align: center;
    font-family: "Noto Sans JP", sans-serif;
    font-size: 8px;
    line-height: 11px;
    color: var(--note-grey);
  }
  .envelope-outline {
    position: absolute;
    top: 0;
    left: 0;
  }
  .brand-name {
    position: absolute;
    top: 226px;
    left: 0;
    width: 100%;
    text-align: center;
    font-size: 24px;
    font-weight: 700;
    color: var(--brand-blue);
    letter-spacing: 0.5px;
  }
  .sender {
    position: absolute;
    top: 982px;
    left: 0;
    width: 100%;
    text-align: center;
    color: var(--brand-blue);
  }
  .sender-company {
    font-size: 21px;
    font-weight: 700;
    margin: 0 0 10px;
    letter-spacing: 0.5px;
  }
  .sender-address {
    font-size: 10.5px;
    line-height: 17px;
    margin: 0;
    font-style: normal;
  }
</style>
</head>
<body>
<div class="sheet">
  <div class="sheet-note">角2封筒 裏面<br>1C</div>

  <svg class="envelope-outline" width="849" height="1200" viewBox="0 0 849 1200" aria-hidden="true">
    <rect x="34.5" y="184.5" width="781" height="948" fill="none" stroke="var(--line)" stroke-width="1"/>
    <polyline points="34.5,184.5 141,283 708,283 815.5,184.5" fill="none" stroke="var(--line)" stroke-width="1"/>
  </svg>

  <div class="brand-name">Kaiho Works</div>

  <div class="sender">
    <p class="sender-company">KAIHO WORKS INC.</p>
    <address class="sender-address">
      Harbor Terrace Minato 502<br>
      3-4-5 Kaigan, Minato-ku, Tokyo 105-0022, Japan<br>
      http://www.kaihoworks.jp
    </address>
  </div>
</div>
</body>
</html>
```